corvane business cards

Hey design gurus!
I'm after a clean, modern, stylish business card for my about to be launched company.
I've uploaded the logos for my company "Corvane Electrical Solutions"
and also the brightway electricians logo to whom i am associated.

```html
<!DOCTYPE html>
<html lang="en">
<head>
<meta charset="utf-8">
<title>Corvane Electrical Solutions — Business Cards</title>
<link href="https://fonts.googleapis.com/css2?family=Montserrat:wght@400;500;700;800&display=swap" rel="stylesheet">
<style>
  :root {
    --backdrop: #3a3a3a;
    --navy: #03141f;
    --navy-soft: #0b2230;
    --blue: #1a8ad6;
    --white: #ffffff;
    --badge-line: #b5584a;
    --divider: #3f5260;
  }
  * { box-sizing: border-box; margin: 0; padding: 0; }
  html, body {
    width: 1200px; height: 1200px; overflow: hidden;
    background: var(--backdrop);
    font-family: "Montserrat", sans-serif;
  }
  .stage { position: relative; width: 1200px; height: 1200px; }

  .card {
    position: absolute; left: 220px;
    width: 760px; height: 434px;
    border-radius: 30px; overflow: hidden;
    box-shadow: 0 18px 40px rgba(0,0,0,.45);
  }
  .card--front { top: 120px; background: var(--white); }
  .card--back {
    top: 640px;
    background: linear-gradient(135deg, var(--navy) 0%, var(--navy-soft) 55%, var(--navy) 100%);
  }

  /* front: top brand zone */
  .brand-zone {
    position: absolute; left: 0; top: 0; width: 100%; height: 230px;
  }
  .brand-lockup {
    position: absolute; left: 60px; top: 62px;
    display: flex; align-items: center; gap: 18px;
  }
  .brand-dot {
    width: 62px; height: 62px; border-radius: 50%;
    border: 6px solid var(--blue);
  }
  .brand-name {
    font-weight: 800; color: var(--blue);
    font-size: 62px; letter-spacing: 2px; line-height: 1;
  }
  .partner-badge {
    position: absolute; left: 300px; top: 150px;
    width: 220px; height: 58px;
    border: 1.5px solid var(--badge-line); border-radius: 6px;
    display: flex; align-items: center; padding-left: 12px;
  }
  .partner-badge__square {
    width: 40px; height: 40px; border-radius: 4px; background: #1d2a4a;
  }

  .accent-rule {
    position: absolute; left: 0; top: 236px; width: 100%; height: 6px;
    background: var(--blue);
  }
  .info-zone {
    position: absolute; left: 0; top: 250px; width: 100%; bottom: 0;
    background: linear-gradient(90deg, var(--navy) 0%, var(--navy) 45%, var(--navy-soft) 70%, var(--navy) 100%);
  }
  .person { position: absolute; left: 60px; top: 70px; }
  .person__name {
    color: var(--blue); font-weight: 500; font-size: 34px; letter-spacing: -.5px; line-height: 1;
  }
  .person__role {
    color: var(--white); font-weight: 400; font-size: 20px; margin-top: 6px;
  }
  .info-divider {
    position: absolute; left: 380px; top: 24px; width: 1px; height: 130px;
    background: var(--divider);
  }
  .contact-list {
    position: absolute; left: 420px; top: 18px; list-style: none;
  }
  .contact-list li {
    display: flex; align-items: flex-start; gap: 10px;
    color: var(--white); font-size: 17px; line-height: 1.25; margin-bottom: 8px;
  }
  .contact-list svg { flex: none; width: 18px; height: 18px; margin-top: 1px; }

  /* back */
  .back-lockup {
    position: absolute; left: 0; right: 0; top: 110px;
    display: flex; flex-direction: column; align-items: center;
  }
  .back-lockup .brand-dot { width: 90px; height: 90px; border-width: 8px; margin-bottom: 22px; }
  .back-lockup .brand-name { font-size: 84px; letter-spacing: 3px; }
  .tagline {
    color: var(--white); font-weight: 700; font-size: 20px; letter-spacing: 6px;
    margin-top: 10px;
  }
</style>
</head>
<body>
<main class="stage">

  <section class="card card--front" aria-label="Business card front">
    <div class="brand-zone">
      <div class="brand-lockup">
        <span class="brand-dot"></span>
        <span class="brand-name">CORVANE</span>
      </div>
      <div class="partner-badge" role="img" aria-label="Brightway Electricians partner badge">
        <span class="partner-badge__square"></span>
      </div>
    </div>
    <div class="accent-rule"></div>
    <div class="info-zone">
      <div class="person">
        <p class="person__name">FULL NAME</p>
        <p class="person__role">POSITION</p>
      </div>
      <div class="info-divider"></div>
      <ul class="contact-list">
        <li>
          <svg viewBox="0 0 24 24" fill="var(--blue)"><path d="M6.6 10.8a15 15 0 0 0 6.6 6.6l2.2-2.2a1 1 0 0 1 1-.25 11.4 11.4 0 0 0 3.6.57 1 1 0 0 1 1 1V20a1 1 0 0 1-1 1A17 17 0 0 1 3 4a1 1 0 0 1 1-1h3.5a1 1 0 0 1 1 1c0 1.25.2 2.45.57 3.57a1 1 0 0 1-.25 1z"/></svg>
          (000) 000 0000
        </li>
        <li>
          <svg viewBox="0 0 24 24" fill="none" stroke="var(--blue)" stroke-width="2"><rect x="2" y="5" width="20" height="14" rx="1"/><path d="M2 6l10 7 10-7"/></svg>
          email@company.com
        </li>
        <li>
          <svg viewBox="0 0 24 24" fill="none" stroke="var(--blue)" stroke-width="1.8"><circle cx="12" cy="12" r="10"/><path d="M2 12h20M12 2c3 3 3 17 0 20M12 2c-3 3-3 17 0 20"/></svg>
          www.company.com
        </li>
        <li>
          <svg viewBox="0 0 24 24" fill="var(--blue)"><path d="M12 2a7 7 0 0 0-7 7c0 5 7 13 7 13s7-8 7-13a7 7 0 0 0-7-7zm0 9.5A2.5 2.5 0 1 1 12 6.5a2.5 2.5 0 0 1 0 5z"/></svg>
          <span>123 Name Street, 000<br>Your City, 00000-000</span>
        </li>
      </ul>
    </div>
  </section>

  <section class="card card--back" aria-label="Business card back">
    <div class="back-lockup">
      <span class="brand-dot"></span>
      <span class="brand-name">CORVANE</span>
      <span class="tagline">ELECTRICAL SOLUTIONS</span>
    </div>
  </section>

</main>
</body>
</html>
```